Organic Infographic – "The 4 Dimensions of Transformation"

Overview:
We are a coaching/education brand (Brightmoor Institute) and need a redesigned infographic illustrating our 4-area transformation model. Our current version (attached) uses a rigid, hard-edged triangle/pyramid layout — we want a completely new visual approach that feels organic, soft, and alive, since the topic is human personal development, not a technical process.

Content structure (please keep the wording, redesign the visual form):

4 areas: "Embodiment – The Foundation" and "Focus & Intuition Redefined – The Lens" sit on the same base level. "Heart Centered Living – The Bridge" sits one level above, connecting/enabling the other two. "Becoming Unlimited – The Peak" sits at the top, made possible by Heart Centered Living.
The 4 areas influence and inspire one another — this mutual connection must be visually recognizable (e.g. through overlapping zones, blended color transitions, connecting flowing lines, or similar). Areas may stay visually distinct; the connection between them is what must be shown.
Hierarchy should be expressed mainly through position/arrangement (ascending flow), not through size differences — all 4 areas should carry similar visual weight, since each is equally essential.
A supporting element: "The Brightmoor Methodology" with 3 phases (Phase 1: Awareness & Insight, Phase 2: Integration & Practice, Phase 3: Expansion & Sustainable Growth), each with a short description (text provided below).

Style direction:
Organic, soft, flowing shapes — no sharp angles or rigid geometric triangles. Attached are 3 moodboard references showing the direction we like: overlapping/blended circular shapes, flowing ribbon-style connections, and organic swirl divisions. Please don't copy any of them directly — combine this organic/overlapping visual language with our specific asymmetric hierarchy (2 areas base level + 1 bridge + 1 peak), which none of the references show exactly. This creative translation is the core task.

Icons: Please design one new, unified icon per area (4 total) plus 3 simple icons for the methodology phases — consistent style across all 7, your creative interpretation is welcome.

Typography: Headlines in Arsenal, body text in DM Sans.

Colors: Base palette — Embodiment D09176, Focus & Intuition Redefined B6623E, Heart Centered Living D9866B, Becoming Unlimited 6F7A70, dark text 23211A, light accent EACEC1. Slight adjustments are welcome if they improve visual distinction between areas.

Technical requirements (important):

Final files as vector format (SVG, AI, or EPS), with separated, editable, non-flattened/non-merged layers and paths.
Shapes should consist of simple, closed outline paths — no fine textures, no complex multi-stop gradients, no photorealistic rendering — since the artwork will later be manually redrawn as a whiteboard-animation video.
Primary format: 16:9 landscape. A secondary vertical/mobile version (3 outer areas stacked below the top area) is welcome but optional.

Usage rights: Full commercial usage across website, video, and social media required.

Attachments to include: current draft PDF (for text content and logo reference only — not for layout), our logo file, and the 3 moodboard reference images.

Budget: $100–150 — please let us know if this realistically allows for more designer participation, or advise on adjusting scope/budget

Methodology phase texts (for the 3 supporting icons):

Phase 1: Awareness & Insight
Cultivating self-reflection, identifying patterns, and gaining clarity on personal drivers through introspective practices and data-informed assessment.

Phase 2: Integration & Practice
Applying tools and frameworks, developing new habits, and aligning actions with core values through consistent application and feedback loops.

Phase 3: Expansion & Sustainable Growth
Achieving long-term transformation, exceeding limitations, and fostering resilience through continuous evolution and a purpose-driven approach.

```html
<!DOCTYPE html>
<html lang="en">
<head>
<meta charset="utf-8">
<title>The 4 Dimensions of Transformation – Brightmoor Institute</title>
<link rel="stylesheet" href="https://fonts.googleapis.com/css2?family=Montserrat:wght@400;600;700&family=Marcellus&family=DM+Sans:wght@400;500&display=swap">
<style>
  :root {
    --stage: #383838;
    --paper: #fdfbfa;
    --peach: #f5e3d8;
    --ink: #23211a;
    --ink-soft: #3a3833;
    --rust: #a8593a;
    --rust-title: #b1603d;
    --peak: #6f7a70;
    --bridge: #d9866b;
    --foundation: #d09176;
    --lens: #b0613e;
    --logo-grey: #8e9590;
    --white: #ffffff;
  }
  * { margin: 0; padding: 0; box-sizing: border-box; }
  html, body { width: 1200px; height: 1200px; overflow: hidden; background: var(--stage); }
  h1, h2, h3 { font-weight: 400; }
  .card {
    position: absolute; left: 89.5px; top: 262px;
    width: 1616px; height: 908px;
    transform: scale(0.6214); transform-origin: 0 0;
    background:
      radial-gradient(ellipse 900px 520px at 0% 100%, var(--peach) 0%, rgba(245,227,216,0) 100%),
      radial-gradient(ellipse 700px 400px at 100% 0%, #ffffff 0%, rgba(255,255,255,0) 100%),
      var(--paper);
    overflow: hidden;
    font-family: "DM Sans", sans-serif;
    color: var(--ink);
  }
  .abs { position: absolute; }

  /* Title */
  .title-rule { left: 50px; top: 48px; width: 16px; height: 110px;
    border-left: 4px solid var(--rust); border-right: 3px solid var(--ink); }
  .title { left: 74px; top: 40px; font-family: "Montserrat", sans-serif; font-weight: 700; }
  .title-main { color: var(--rust); font-size: 60px; line-height: 1; white-space: nowrap; }
  .title-main .num { font-size: 92px; font-weight: 600; vertical-align: -4px; margin: 0 14px; }
  .title-sub { color: var(--ink); font-size: 45px; letter-spacing: 2.5px; line-height: 1; margin-top: 4px; white-space: nowrap; }

  /* Brand */
  .brand { left: 1143px; top: 48px; display: flex; align-items: center; gap: 13px; }
  .brand-dot { width: 80px; height: 80px; border-radius: 50%; background: var(--foundation); flex: none; }
  .brand-name { font-family: "DM Sans", sans-serif; font-size: 34px; color: var(--logo-grey); font-weight: 400; white-space: nowrap; }

  /* Dimension shapes */
  .dimensions { left: 0; top: 0; width: 1616px; height: 908px; }

  .dim-title { font-family: "Marcellus", "Arsenal", serif; font-weight: 400; font-size: 24px; line-height: 1.1; color: var(--ink); white-space: nowrap; }
  .dim-title .role { color: var(--white); }
  .dim-body { font-size: 14px; line-height: 1.35; color: var(--ink); white-space: nowrap; margin-top: 8px; }
  .on-dark .dim-body { color: var(--white); }

  .peak { left: 659px; top: 176px; width: 320px; text-align: center; }
  .peak .dim-title { font-size: 23px; }
  .bridge { left: 722px; top: 326px; }
  .bridge .dim-title { font-size: 25px; }
  .bridge .dim-title .role { padding-left: 50px; }
  .bridge .dim-body { margin-left: -43px; }
  .foundation { left: 424px; top: 468px; }
  .foundation .dim-title { font-size: 27px; }
  .lens { left: 938px; top: 484px; width: 268px; }
  .lens .dim-title { padding-left: 69px; }
  .lens .dim-body { text-align: right; }

  /* Methodology */
  .method-heading { left: 74px; top: 670px; font-family: "Montserrat", sans-serif; font-weight: 400; font-size: 47px; color: var(--ink-soft); white-space: nowrap; }
  .phase-icon { position: absolute; }
  .phase-title { font-size: 20px; font-weight: 400; color: var(--rust-title); white-space: nowrap; line-height: 1.2; }
  .phase-body { font-size: 14.5px; line-height: 1.28; color: var(--ink); white-space: nowrap; margin-top: 2px; }
  .phase-1 { left: 172px; top: 765px; }
  .phase-2 { left: 646px; top: 759px; }
  .phase-3 { left: 1141px; top: 757px; }
</style>
</head>
<body>
<main class="card">

  <div class="abs title-rule"></div>
  <h1 class="abs title">
    <div class="title-main">The<span class="num">4</span>Dimensions</div>
    <div class="title-sub">OF TRANSFORMATION</div>
  </h1>

  <div class="abs brand">
    <span class="brand-dot"></span>
    <span class="brand-name">Brightmoor Institute</span>
  </div>

  <svg class="abs dimensions" viewBox="0 0 1616 908" aria-hidden="true">
    <!-- Peak -->
    <circle cx="821" cy="276" r="163" fill="none" stroke="var(--peak)" stroke-width="2.5"/>
    <circle cx="821" cy="280" r="157" fill="var(--peak)"/>

    <!-- Bridge -->
    <path d="M600 330 C640 290 720 280 790 292 C850 302 880 322 930 322 C980 322 1020 292 1050 300 C1085 312 1088 380 1075 420 C1060 470 1000 485 940 470 C870 450 820 440 760 445 C700 450 620 490 580 450 C555 420 570 360 600 330 Z"
          fill="none" stroke="var(--bridge)" stroke-width="2.5" transform="translate(820 380) scale(1.035 1.06) translate(-820 -380)"/>
    <path d="M600 330 C640 290 720 280 790 292 C850 302 880 322 930 322 C980 322 1020 292 1050 300 C1085 312 1088 380 1075 420 C1060 470 1000 485 940 470 C870 450 820 440 760 445 C700 450 620 490 580 450 C555 420 570 360 600 330 Z"
          fill="var(--bridge)" fill-opacity="0.95"/>

    <!-- Foundation -->
    <path d="M380 470 C400 420 450 400 530 403 C620 407 720 440 790 470 C830 490 830 530 790 560 C720 600 620 620 530 622 C440 624 380 590 370 540 C366 515 370 490 380 470 Z"
          fill="none" stroke="var(--foundation)" stroke-width="2.5" transform="translate(600 512) scale(1.03 1.06) translate(-600 -512)"/>
    <path d="M380 470 C400 420 450 400 530 403 C620 407 720 440 790 470 C830 490 830 530 790 560 C720 600 620 620 530 622 C440 624 380 590 370 540 C366 515 370 490 380 470 Z"
          fill="var(--foundation)" fill-opacity="0.92"/>

    <!-- Lens -->
    <path d="M800 545 C810 500 900 470 980 440 C1060 410 1130 395 1180 400 C1240 408 1268 460 1266 520 C1262 580 1220 620 1150 622 C1060 624 960 610 880 595 C820 583 795 570 800 545 Z"
          fill="none" stroke="var(--lens)" stroke-width="2.5" transform="translate(1034 512) scale(1.025 1.06) translate(-1034 -512)"/>
    <path d="M800 545 C810 500 900 470 980 440 C1060 410 1130 395 1180 400 C1240 408 1268 460 1266 520 C1262 580 1220 620 1150 622 C1060 624 960 610 880 595 C820 583 795 570 800 545 Z"
          fill="var(--lens)" fill-opacity="0.94"/>

    <!-- Icons -->
    <g class="icon-peak" fill="none" stroke="var(--white)" stroke-width="2" stroke-linecap="round" stroke-linejoin="round">
      <polyline points="804,172 818,156 826,164 842,146"/>
      <polyline points="834,146 842,146 842,154"/>
    </g>
    <path class="icon-bridge" d="M689 368 C670 354 664 346 666 336 C668 326 682 322 689 332 C696 322 710 326 712 336 C714 346 708 354 689 368 Z"
          fill="none" stroke="var(--ink)" stroke-width="2.2" stroke-linejoin="round"/>
    <circle class="icon-foundation" cx="506" cy="438" r="20" fill="none" stroke="var(--ink)" stroke-width="1.6" role="img" aria-label="Seated meditation icon"/>
    <g class="icon-lens" fill="none" stroke="var(--white)" stroke-width="2" stroke-linecap="round">
      <path d="M1132 448 C1150 426 1170 426 1188 448 C1170 470 1150 470 1132 448 Z"/>
      <circle cx="1160" cy="448" r="10"/>
      <line x1="1160" y1="418" x2="1160" y2="426"/>
      <line x1="1160" y1="470" x2="1160" y2="478"/>
      <line x1="1137" y1="425" x2="1142" y2="430"/>
      <line x1="1183" y1="425" x2="1178" y2="430"/>
      <line x1="1137" y1="471" x2="1142" y2="466"/>
      <line x1="1183" y1="471" x2="1178" y2="466"/>
    </g>
  </svg>

  <section class="abs peak on-dark">
    <h2 class="dim-title">Becoming Unlimited<br><span class="role">– The Peak</span></h2>
    <p class="dim-body">Lorem ipsum dolor sit amet,<br>consectetuer adipiscing elit.</p>
  </section>

  <section class="abs bridge">
    <h2 class="dim-title">Heart Centered Living<br><span class="role">– The Bridge</span></h2>
    <p class="dim-body">Lorem ipsum dolor sit amet, consectetuer<br>adipiscing elit, sed diam nonummy nibh.</p>
  </section>

  <section class="abs foundation">
    <h2 class="dim-title">Embodiment<br><span class="role">– The Foundation</span></h2>
    <p class="dim-body">Lorem ipsum dolor sit amet, consectetuer<br>adipiscing elit, sed diam nonummy nibh<br>euismod tincidunt adipiscing</p>
  </section>

  <section class="abs lens on-dark">
    <h2 class="dim-title">Focus &amp; Intuition<br>Redefined <span class="role">– The Lens</span></h2>
    <p class="dim-body">Lorem ipsum dolor sit amet, consectetuer<br>adipiscing elit, sed diam nonummy nibh<br>euismod tincidunt adipiscing</p>
  </section>

  <h2 class="abs method-heading">The Brightmoor Methodology</h2>

  <svg class="abs phase-icon" style="left:74px;top:762px" width="76" height="86" viewBox="0 0 76 86" aria-hidden="true">
    <g fill="none" stroke="var(--rust)" stroke-width="2.2" stroke-linecap="round" stroke-linejoin="round">
      <circle cx="34" cy="32" r="16"/>
      <circle cx="34" cy="32" r="6"/>
      <path d="M34 12 V16 M34 48 V52 M14 32 H18 M50 32 H54 M20 18 L23 21 M45 43 L48 46 M48 18 L45 21 M23 43 L20 46"/>
      <path d="M14 84 V66 C6 58 4 48 6 38 C10 14 30 4 48 8 C64 12 72 26 70 40 L74 52 L68 54 V64 C68 70 62 72 56 70 V84"/>
    </g>
  </svg>
  <svg class="abs phase-icon" style="left:553px;top:750px" width="62" height="100" viewBox="0 0 62 100" aria-hidden="true">
    <g fill="none" stroke="var(--rust)" stroke-width="2.2" stroke-linecap="round" stroke-linejoin="round">
      <path d="M18 64 C18 54 4 46 4 30 C4 15 16 4 31 4 C46 4 58 15 58 30 C58 46 44 54 44 64 Z"/>
      <path d="M31 44 C22 37 18 33 19 27 C20 21 28 19 31 25 C34 19 42 21 43 27 C44 33 40 37 31 44 Z"/>
      <path d="M18 72 H44 M18 80 H44 M22 88 H40 M27 95 H35"/>
    </g>
  </svg>
  <svg class="abs phase-icon" style="left:1036px;top:752px" width="92" height="96" viewBox="0 0 92 96" aria-hidden="true">
    <g fill="none" stroke="var(--rust)" stroke-width="2.2" stroke-linecap="round" stroke-linejoin="round">
      <path d="M30 4 H60 C63 4 64 6 64 8 V26 C64 28 63 30 60 30 H40 L32 38 V30 H30 C27 30 26 28 26 26 V8 C26 6 27 4 30 4 Z"/>
      <path d="M34 13 H56 M34 21 H50"/>
      <circle cx="14" cy="56" r="6"/><circle cx="46" cy="62" r="6"/><circle cx="78" cy="56" r="6"/>
      <path d="M2 80 C2 70 26 70 26 80 M34 92 C34 80 58 80 58 92 M66 80 C66 70 90 70 90 80"/>
    </g>
  </svg>

  <section class="abs phase-1">
    <h3 class="phase-title">Phase 1: Awareness &amp; Insight</h3>
    <p class="phase-body">Cultivating self-reflection, identifying patterns<br>and gaining clarity on personal drivers through<br>introspective practices and data-informed assessment.</p>
  </section>
  <section class="abs phase-2">
    <h3 class="phase-title">Phase 2: Integration &amp; Practice</h3>
    <p class="phase-body">Applying tools and frameworks, developing new habits<br>and aligning actions with core values through consistent<br>application and feedback loops.</p>
  </section>
  <section class="abs phase-3">
    <h3 class="phase-title">Phase 3: Expansion &amp; Sustainable Growth</h3>
    <p class="phase-body">Achieving long-term transformation, exceeding limitations<br>and fostering resilience through continuous evolution and<br>a purpose-driven approach.</p>
  </section>

</main>
</body>
</html>
```